Decorative concrete business needs new business cards

Our company attracts homeowners and business with disposable cash. We are a artistic decorative coatings company that will transform your driveway, patio, floors or counter tops into a work of art. We also engrave logos and designs right into the concrete! We are upscale and very professional company. I am open for rearranging our logo on the business card and also to different color patterns. We like the blue and black as in BrushNest's logo. We also like blue and orange/yellow.

Target Market(s)

Adults 30-70

Industry/Entity Type

Concrete

Contact Information for Business Card

Simple: Name, phone, email, website and social media icons

Font styles to use
Serif

Colors

Designer to choose colors to be used in the design.

Requirements
Must have
• Must present a professional upscale appearance. I have attached before and after photos that show you what our industry does. Maybe I will have before and after photo on back of card.
Nice to have
• Artistic, but bold. Nothing whimsical or cute.
Should not have
• Should not have cartoon or childlike appearance.

```html
<!DOCTYPE html>
<html lang="en">
<head>
<meta charset="utf-8">
<title>Stoneleaf Finishes – Business Card</title>
<link href="https://fonts.googleapis.com/css2?family=Cinzel:wght@500&family=Open+Sans:wght@400&display=swap" rel="stylesheet">
<style>
  :root {
    --page: #e9e6e1;
    --card-white: #ffffff;
    --charcoal: #262626;
    --brand-blue: #1a7cc1;
    --text-light: #f2f2f2;
    --label-bg: #222222;
    --concrete: #8e8b85;
    --stamped: #8a7150;
    --house: #5e5245;
  }
  * { box-sizing: border-box; margin: 0; padding: 0; }
  html, body { width: 1200px; height: 1000px; overflow: hidden; }
  body { background: var(--page); position: relative; font-family: "Open Sans", Arial, sans-serif; }

  .card { position: absolute; left: 266px; width: 666px; height: 397px; overflow: hidden; box-shadow: 0 4px 14px rgba(0,0,0,.25); }
  .card--front { top: 74px; background: var(--card-white); }
  .card--back { top: 534px; }

  .front__panel { position: absolute; inset: 0; }

  .brand { position: absolute; display: flex; align-items: center; gap: 14px; }
  .brand__square { width: 62px; height: 62px; background: var(--charcoal); flex: none; }
  .brand__name { font-family: "Cinzel", "Times New Roman", serif; font-weight: 500; line-height: 1.02; letter-spacing: .04em; }
  .card--front .brand { left: 32px; top: 146px; }
  .card--front .brand__name { color: var(--brand-blue); font-size: 34px; }

  .contact { position: absolute; right: 32px; top: 84px; text-align: right; color: var(--text-light); font-size: 16.5px; line-height: 1.5; }
  .contact__name { font-family: "Cinzel", "Times New Roman", serif; font-weight: 500; color: var(--brand-blue); font-size: 21px; letter-spacing: .03em; line-height: 1.2; }
  .contact__title { margin-bottom: 18px; }
  .contact__address { margin-bottom: 18px; }
  .contact__row { display: flex; justify-content: flex-end; align-items: center; gap: 7px; height: 25px; }
  .contact__row svg { width: 15px; height: 15px; flex: none; }
  .contact__social { margin-top: 14px; }
  .social-dot { width: 16px; height: 16px; border-radius: 50%; background: var(--brand-blue); flex: none; }

  .front__marker { position: absolute; right: 0; top: 96px; width: 0; height: 0; border-top: 12px solid transparent; border-bottom: 12px solid transparent; border-right: 17px solid var(--card-white); }

  .back__photo { position: absolute; inset: 0;
    background:
      linear-gradient(180deg, rgba(70,60,50,.85) 0%, rgba(94,82,69,.55) 38%, rgba(0,0,0,0) 60%),
      linear-gradient(90deg, var(--concrete) 0%, #9a968f 45%, var(--stamped) 50%, #9a7f5a 100%); }
  .card--back .brand { left: 178px; top: 92px; }
  .card--back .brand__square { background: var(--text-light); }
  .card--back .brand__name { color: var(--text-light); font-size: 36px; }

  .tag { position: absolute; top: 261px; width: 111px; height: 36px; background: var(--label-bg); color: var(--text-light); font-size: 25px; display: flex; align-items: center; justify-content: center; }
  .tag--before { left: 112px; }
  .tag--after { left: 440px; }
  .tag-leaders { position: absolute; inset: 0; }
</style>
</head>
<body>

<section class="card card--front" aria-label="Business card front">
  <svg class="front__panel" viewBox="0 0 666 397" width="666" height="397" aria-hidden="true">
    <polygon points="440,0 666,0 666,397 297,397" fill="var(--charcoal)"/>
  </svg>
  <div class="front__marker"></div>

  <div class="brand">
    <span class="brand__square"></span>
    <span class="brand__name">Stoneleaf<br>Finishes</span>
  </div>

  <div class="contact">
    <p class="contact__name">DORAN QUELL</p>
    <p class="contact__title">Managing Director</p>
    <p class="contact__address">418 North Alder Lane<br>Fairmont, MD 21700</p>
    <div class="contact__row">+ 000 000 0000
      <svg viewBox="0 0 16 16"><path fill="var(--brand-blue)" d="M2 6c0-2 3-3 6-3s6 1 6 3v1h-3V6H5v1H2zM4 8h8l1 5H3z"/></svg>
    </div>
    <div class="contact__row">info@stoneleaffinishes.com
      <svg viewBox="0 0 16 16"><rect x="1" y="3.5" width="14" height="9.5" fill="var(--brand-blue)"/><path d="M1.5 4l6.5 5 6.5-5" stroke="var(--charcoal)" stroke-width="1.2" fill="none"/></svg>
    </div>
    <div class="contact__row">www.stoneleaffinishes.com
      <svg viewBox="0 0 16 16"><circle cx="8" cy="8" r="6.3" fill="none" stroke="var(--brand-blue)" stroke-width="1.6"/><path d="M1.7 8h12.6M8 1.7c-3 3.5-3 9 0 12.6M8 1.7c3 3.5 3 9 0 12.6" stroke="var(--brand-blue)" stroke-width="1.1" fill="none"/></svg>
    </div>
    <div class="contact__row contact__social">@stoneleaffinishes <span class="social-dot"></span></div>
  </div>
</section>

<section class="card card--back" aria-label="Business card back">
  <div class="back__photo" role="img" aria-label="Photo of a house with a two-car garage and driveway, the left half plain cracked concrete, the right half finished in stamped decorative stone coating"></div>

  <div class="brand">
    <span class="brand__square"></span>
    <span class="brand__name">Stoneleaf<br>Finishes</span>
  </div>

  <svg class="tag-leaders" viewBox="0 0 666 397" width="666" height="397" aria-hidden="true">
    <line x1="114" y1="296" x2="76" y2="344" stroke="var(--label-bg)" stroke-width="1.2"/>
    <circle cx="76" cy="344" r="4.5" fill="var(--label-bg)"/>
    <line x1="549" y1="297" x2="586" y2="344" stroke="var(--label-bg)" stroke-width="1.2"/>
    <circle cx="586" cy="344" r="4.5" fill="var(--label-bg)"/>
  </svg>
  <div class="tag tag--before">BEFORE</div>
  <div class="tag tag--after">AFTER</div>
</section>

</body>
</html>
```